Lawyers in the Netherlands website + logo

We are going in 2015 to launch a website where all law firms in the Netherlands and have the opportunity to place an ad program.

The domain name wil be:

kantoorvinder.website

We want a responsive PSD bootstrap twitter 1170 pixel grid.
for the homepage, result page and the detail page of the customer.

This sites we like:
https://www.qorvantis.com/lawyers

https://lawyers.qorvantis.com/lawyer/tim-garsby-7305826

http://solicitordirectory.brevimark.co.uk/
Map of the Netherlands?

http://solicitordirectory.brevimark.co.uk/listing/category-search/commercial
http://www.tandelvo.com.au/find-a-lawyer/banking-finance-law/

```html
<!DOCTYPE html>
<html lang="en">
<head>
<meta charset="utf-8">
<title>Kantoorvinder</title>
<link rel="stylesheet" href="https://fonts.googleapis.com/css2?family=Open+Sans:wght@400;600;700&display=swap">
<style>
:root{
  --navy:#1b3466;
  --navy-deep:#14295a;
  --navy-bar:#20407c;
  --orange:#e8731a;
  --ink:#333a44;
  --muted:#666b73;
  --heading:#132e63;
  --rule:#c9ccd2;
  --white:#ffffff;
}
*{margin:0;padding:0;box-sizing:border-box}
html,body{width:672px;height:1200px;overflow:hidden}
body{font-family:"Open Sans",Arial,sans-serif;color:var(--ink);background:var(--white);position:relative}
ul{list-style:none}
.abs{position:absolute}

/* header */
.site-header{position:absolute;left:0;top:0;width:672px;height:39px;background:var(--navy)}
.brand{position:absolute;left:63px;top:10px;display:flex;align-items:center;gap:6px;color:var(--white);font-weight:700;font-size:15px;letter-spacing:.2px}
.brand-mark{width:14px;height:14px;background:var(--white)}
.btn{display:inline-flex;align-items:center;justify-content:center;background:var(--orange);color:var(--white);font-weight:600}
.btn-listed{position:absolute;left:516px;top:9px;width:94px;height:20px;font-size:9px}
.header-rule{position:absolute;left:0;top:39px;width:672px;height:2px;background:var(--orange)}
.main-nav{position:absolute;left:0;top:41px;width:672px;height:14px;background:var(--navy-bar);font-size:6.6px;color:var(--white)}
.main-nav a{position:absolute;top:3px;color:var(--white);text-decoration:none}
.main-nav a.active{color:var(--orange)}

/* hero */
.hero-photo{position:absolute;left:0;top:55px;width:672px;height:295px;background:linear-gradient(100deg,#9aa3ad 0%,#dcdfe2 30%,#c9b8a8 55%,#e8e4dc 75%,#b9c0c6 100%)}
.search-panel{position:absolute;left:55px;top:224px;width:562px;height:83px;background:rgba(27,52,102,.82)}
.hero-title{position:absolute;left:52px;top:6px;color:var(--white);font-size:22px;font-weight:400}
.search-field{position:absolute;top:46px;height:24px;background:var(--white);border:2px solid #d9dce0;font-size:10px;display:flex;align-items:center;padding-left:8px}
.field-issue{left:49px;width:240px;color:#9a9ea4}
.field-in{position:absolute;left:307px;top:55px;font-size:6.5px;color:#c8d0de}
.field-city{left:327px;width:156px;color:var(--ink);font-weight:600;font-size:10.5px}
.field-city svg{position:absolute;right:8px;top:8px}
.btn-search{position:absolute;left:441px;top:45px;width:70px;height:26px;font-size:10px;gap:4px}

/* tabs */
.tab-band{position:absolute;left:0;top:350px;width:672px;height:32px;background:var(--navy)}
.tab{position:absolute;top:10px;height:21px;width:187px;background:#f4f4f4;border:1px solid #cfd3d8;font-size:11.5px;color:#4a4f56;padding:3px 7px;font-weight:600}
.tab.active{background:var(--orange);color:var(--white);border-color:var(--orange)}
.tab-rule{position:absolute;left:0;top:381px;width:672px;height:2px;background:var(--orange)}

/* practice areas */
.section-label{position:absolute;left:62px;top:394px;font-size:9.5px;font-weight:700;color:var(--heading)}
.area-list{position:absolute;top:416px;font-size:7.6px;line-height:13.44px;color:var(--ink)}

/* info band */
.info-band{position:absolute;left:0;top:688px;width:672px;height:209px;background:linear-gradient(90deg,#13306a 0%,#1f3e7a 50%,#13306a 100%)}
.info-title{position:absolute;left:0;top:44px;width:672px;text-align:center;color:var(--white);font-size:14.5px;font-weight:600}
.info-item{position:absolute;top:96px;width:180px;text-align:center;color:var(--white)}
.info-item svg{display:block;margin:0 auto}
.info-item h3{font-size:11.5px;font-weight:400;margin-top:6px}
.info-item p{font-size:6.3px;line-height:10px;margin-top:2px}

/* claim */
.claim-title{position:absolute;left:0;top:923px;width:672px;text-align:center;font-size:13.5px;font-weight:600;color:var(--heading)}
.claim-text{position:absolute;left:108px;top:952px;width:456px;text-align:center;font-size:7.4px;line-height:12px;color:var(--muted)}
.btn-claim{position:absolute;left:283px;top:996px;width:106px;height:27px;font-size:10px;font-weight:400}
.footer-rule{position:absolute;left:62px;top:1050px;width:548px;height:1px;background:var(--rule)}

/* footer */
.footer-col{position:absolute;top:1075px}
.footer-col h4{font-size:10px;font-weight:700;color:var(--heading);margin-bottom:5px}
.footer-col li{font-size:7.3px;line-height:13.44px;color:var(--muted)}
.newsletter-note{font-size:6px;color:var(--muted);margin-top:-4px}
.newsletter-form{display:flex;margin-top:4px}
.newsletter-input{width:90px;height:15px;border:1px solid #cfd3d8;font-size:5.5px;color:#9a9ea4;padding:4px 5px}
.newsletter-send{width:29px;height:15px;font-size:6px;font-weight:400}
.social h4{margin-top:10px;margin-bottom:4px}
.social-row{display:flex;gap:5px}
.social-dot{width:14px;height:14px;border-radius:50%;background:var(--navy-bar)}
.bottom-bar{position:absolute;left:0;top:1178px;width:672px;height:22px;background:var(--navy);color:var(--white);font-size:6.2px}
.bottom-bar span{position:absolute;top:8px}
</style>
</head>
<body>

<header class="site-header">
  <div class="brand"><span class="brand-mark"></span>KANTOORVINDER</div>
  <a class="btn btn-listed">Lawyers Get Listed</a>
</header>
<div class="header-rule"></div>
<nav class="main-nav">
  <a class="active" style="left:67px">Home</a>
  <a style="left:104px">Find A Lawyer</a>
  <a style="left:165px">Question &amp; Answers</a>
  <a style="left:246px">Legal Practice Centers</a>
  <a style="left:332px">Code, Regulations &amp; Case Law</a>
  <a style="left:552px">Sign in</a>
</nav>

<section class="hero-photo" role="img" aria-label="Photo of a smiling couple meeting with a lawyer at a desk"></section>
<div class="search-panel">
  <h1 class="hero-title">Helping you with your legal needs</h1>
  <div class="search-field field-issue">Search Legal Issue or Lawyer Name</div>
  <span class="field-in">in</span>
  <div class="search-field field-city" style="width:100px;left:327px">Amsterdam
    <svg width="8" height="6" viewBox="0 0 8 6"><path d="M0 0h8L4 6z" fill="#e8731a"/></svg>
  </div>
  <a class="btn btn-search">
    <svg width="12" height="12" viewBox="0 0 12 12"><circle cx="5" cy="5" r="3.6" fill="none" stroke="#fff" stroke-width="1.6"/><path d="M7.6 7.6l3.4 3.4" stroke="#fff" stroke-width="2"/></svg>SEARCH
  </a>
</div>

<div class="tab-band">
  <div class="tab" style="left:55px">Find Lawyer by Location</div>
  <div class="tab active" style="left:243px">Find Lawyers by Practice Area</div>
  <div class="tab" style="left:430px">Legal Information Issues</div>
</div>
<div class="tab-rule"></div>

<h2 class="section-label">Select Practice Area</h2>
<ul class="area-list" style="left:62px">
  <li>Bankruptcy</li><li>Business Law</li><li>Consumer Law</li><li>Criminal Law</li><li>Divorce</li><li>DUI &amp; DWI</li><li>Employment Law</li><li>Estate Planning</li><li>Family Law</li><li>Foreclosure Defense</li><li>Immigration Law</li><li>Intellectual Property</li><li>Medical Malpractice</li><li>Nursing Home Abuse &amp; Neglect</li><li>Personal Injury</li><li>Probate</li><li>Products Liability</li><li>Real Estate Law</li>
</ul>
<ul class="area-list" style="left:203px">
  <li>Tax Law</li><li>Traffic Tickets</li><li>Workers' Compensation</li><li>Agricultural Law</li><li>Animal &amp; Dog Law</li><li>Antitrust</li><li>Appeals &amp; Appellate</li><li>Arbitration &amp; Mediation</li><li>Asbestos &amp; Mesothelioma</li><li>Broker Fraud</li><li>Civil Rights</li><li>Collections</li><li>Communications &amp; Internet Law</li><li>Construction Law</li><li>Domestic Violence</li><li>Education Law</li><li>Elder Law</li><li>Energy, Oil and Gas</li>
</ul>
<ul class="area-list" style="left:343px">
  <li>Entertainment &amp; Sports</li><li>Environmental Law</li><li>Gov &amp; Administrative Law</li><li>Health Care Law</li><li>Insurance Claims</li><li>Insurance Defense</li><li>International Law</li><li>Juvenile Law</li><li>Landlord Tenant</li><li>Legal Malpractice</li><li>Maritime</li><li>Military Law</li><li>Municipal Law</li><li>Native American Law</li><li>Patents</li><li>Securities Law</li><li>Social Security Disability/SSI</li><li>Trademarks</li>
</ul>
<ul class="area-list" style="left:484px">
  <li>Landlord Tenant</li><li>Legal Malpractice</li><li>Maritime</li><li>Military Law</li><li>Municipal Law</li><li>Native American Law</li><li>Patents</li><li>Securities Law</li><li>Social Security Disability/SSI</li><li>Trademarks</li><li>White Collar Crime</li>
</ul>

<section class="info-band" role="img" aria-label="Faint photo of business people shaking hands in an office, tinted navy">
  <h2 class="info-title">Free Legal Information on Kantoorvinder</h2>
  <div class="info-item" style="left:59px">
    <svg width="38" height="32" viewBox="0 0 38 32"><path d="M2 3h20a2 2 0 0 1 2 2v11a2 2 0 0 1-2 2H10l-6 5v-5H2a2 2 0 0 1-2-2V5a2 2 0 0 1 2-2z" fill="#fff"/><path d="M27 10h8a2 2 0 0 1 2 2v10a2 2 0 0 1-2 2h-2v5l-6-5H16a2 2 0 0 1-2-2v-2h9a4 4 0 0 0 4-4z" fill="#fff"/></svg>
    <h3>Questions &amp; Answers</h3>
    <p>Proin gravida nibh vel velit auctor aliquet enean sollicitudi lorem quis bibendum auctor nisi elit consequat.</p>
  </div>
  <div class="info-item" style="left:246px">
    <svg width="36" height="32" viewBox="0 0 36 32"><path d="M18 0l17 7H1z" fill="#fff"/><rect x="3" y="8" width="30" height="2" fill="#fff"/><rect x="6" y="11" width="3" height="14" fill="#fff"/><rect x="13" y="11" width="3" height="14" fill="#fff"/><rect x="20" y="11" width="3" height="14" fill="#fff"/><rect x="27" y="11" width="3" height="14" fill="#fff"/><rect x="2" y="26" width="32" height="2" fill="#fff"/><rect x="0" y="29" width="36" height="3" fill="#fff"/></svg>
    <h3>Legal Practice Centers</h3>
    <p>Proin gravida nibh vel velit auctor aliquet enean sollicitudi lorem quis bibendum auctor nisi elit consequat.</p>
  </div>
  <div class="info-item" style="left:433px">
    <svg width="32" height="32" viewBox="0 0 32 32"><path d="M11 8V4h10v4" fill="none" stroke="#fff" stroke-width="2"/><rect x="1" y="8" width="30" height="20" rx="2" fill="#fff"/><rect x="8" y="8" width="2" height="20" fill="#bfc8d8"/><rect x="22" y="8" width="2" height="20" fill="#bfc8d8"/></svg>
    <h3>Codes, Regulations &amp; Case Law</h3>
    <p>Proin gravida nibh vel velit auctor aliquet enean sollicitudi lorem quis bibendum auctor nisi elit consequat.</p>
  </div>
</section>

<h2 class="claim-title">Are you a Lawyer? Claim and Keep your Profile Updated</h2>
<p class="claim-text">Proin gravida nibh vel velit auctor aliquet enean sollicitudi lorem quis bibendum auctor nisi elit consequat ipsum nec sagittis sem nibh id elit uis sed odio sit amet nibh vulputate cursus a sit amet mauris.</p>
<a class="btn btn-claim">Get Listed Now</a>
<div class="footer-rule"></div>

<footer>
  <div class="footer-col" style="left:63px">
    <h4>About Us</h4>
    <ul><li>Company History</li><li>Privacy</li><li>Careers</li><li>Community Guidelines</li><li>Media</li></ul>
  </div>
  <div class="footer-col" style="left:194px">
    <h4>Legal Information</h4>
    <ul><li>Questions &amp; Answers</li><li>Legal Practice Center</li><li>Code &amp; Regulation</li><li>Case Law</li><li>How to choose a lawyer</li></ul>
  </div>
  <div class="footer-col" style="left:359px">
    <h4>Lawyers</h4>
    <ul><li>Get Listed</li><li>Update Profile</li><li>Get Support</li><li>Contact Us</li><li>Terms &amp; Conditions</li></ul>
  </div>
  <div class="footer-col" style="left:491px">
    <h4>Newsletter</h4>
    <p class="newsletter-note">Get the latest News &amp; Listing</p>
    <div class="newsletter-form"><div class="newsletter-input">Your Email Address</div><a class="btn newsletter-send">Send</a></div>
    <div class="social">
      <h4>Connect with us</h4>
      <div class="social-row"><span class="social-dot"></span><span class="social-dot"></span><span class="social-dot"></span><span class="social-dot"></span></div>
    </div>
  </div>
</footer>

<div class="bottom-bar">
  <span style="left:61px">Kantoorvinder © 2015 All Rights Reserved</span>
  <span style="left:307px">Find A Lawyer</span>
  <span style="left:364px">Question &amp; Answers</span>
  <span style="left:439px">Legal Practice Centers</span>
  <span style="left:519px">Code, Regulations &amp; Case Law</span>
</div>

</body>
</html>
```